Communication Skill: NODE Assist

I need a Design for a skill I teach to youth. That's why the title NODE Assist. NODE stands for Thoughts, Emotions, Concerns, Hopes & Desires. Under each word are some examples that are meant to help people discuss certain things. I tried to create something myself but want something much more creative and dynamic. I have attached what I designed because it has the information I need in the design. Want it to have a techie look to it.

```html
<!DOCTYPE html>
<html lang="en">
<head>
<meta charset="utf-8">
<title>NODE Assist – Communication Skill</title>
<link href="https://fonts.googleapis.com/css2?family=Montserrat:wght@300;400;800;900&display=swap" rel="stylesheet">
<style>
  :root {
    --bg: #ffffff;
    --thoughts-a: #079b98;
    --thoughts-b: #067c80;
    --hopes-a: #26c4f3;
    --hopes-b: #0597dc;
    --emotions-a: #f39150;
    --emotions-b: #d95e27;
    --concerns-a: #88d1c3;
    --concerns-b: #06b6a8;
    --hub-light: #e3e4e6;
    --hub-mid: #c6c7c9;
    --ring: #c9cacc;
    --node: #d3d4d6;
    --text: #ffffff;
  }
  * { box-sizing: border-box; margin: 0; padding: 0; }
  html, body { width: 1142px; height: 1200px; overflow: hidden; background: var(--bg); }
  body { font-family: "Montserrat", Arial, sans-serif; }
  .canvas { position: relative; width: 1142px; height: 1200px; }
  .wiring { position: absolute; inset: 0; }

  .card {
    position: absolute;
    border-radius: 42px;
    color: var(--text);
    text-align: center;
    box-shadow: 8px 10px 14px rgba(0,0,0,0.18);
    padding-top: 24px;
  }
  .card--thoughts { left: 191px; top: 195px; width: 328px; height: 185px; background: linear-gradient(90deg, var(--thoughts-a), var(--thoughts-b)); }
  .card--hopes { left: 589px; top: 195px; width: 340px; height: 185px; background: linear-gradient(90deg, var(--hopes-a), var(--hopes-b)); }
  .card--emotions { left: 213px; top: 824px; width: 327px; height: 185px; background: linear-gradient(90deg, var(--emotions-a), var(--emotions-b)); padding-top: 20px; }
  .card--concerns { left: 605px; top: 824px; width: 338px; height: 185px; background: linear-gradient(90deg, var(--concerns-a), var(--concerns-b)); }

  .card__title { font-weight: 800; font-size: 23px; letter-spacing: 0.3px; line-height: 1; margin-bottom: 14px; }
  .card--hopes .card__title { margin-bottom: 8px; }
  .card--emotions .card__title { margin-bottom: 5px; }
  .card--concerns .card__title { margin-bottom: 13px; }
  .card__row { font-size: 20px; line-height: 27px; white-space: nowrap; letter-spacing: -0.3px; }
  .card--emotions .card__row { font-size: 18.5px; line-height: 24.5px; }
  .prompt { font-weight: 300; margin: 0 7px; }
  .prompt--strong { font-weight: 800; }

  .hub {
    position: absolute; left: 320px; top: 523px; width: 536px; height: 167px;
    border-radius: 84px;
    background: linear-gradient(180deg, var(--hub-mid), var(--hub-light));
    box-shadow: 10px 14px 20px rgba(0,0,0,0.12);
    display: flex; align-items: center; justify-content: center;
  }
  .hub__title {
    font-weight: 900; font-size: 56px; color: #ffffff; letter-spacing: -0.5px;
    text-shadow: 3px 5px 8px rgba(0,0,0,0.45);
  }
</style>
</head>
<body>
<main class="canvas">
  <svg class="wiring" width="1142" height="1200" viewBox="0 0 1142 1200" aria-hidden="true">
    <path d="M496 493 H420 A138 113 0 0 0 420 720 H496" fill="none" stroke="var(--ring)" stroke-width="5"/>
    <path d="M680 493 H756 A138 113 0 0 1 756 720 H680" fill="none" stroke="var(--ring)" stroke-width="5"/>

    <path d="M290 408 Q290 441 320 441 H516 Q536 441 536 461 V493" fill="none" stroke="var(--thoughts-b)" stroke-width="2.5"/>
    <circle cx="290" cy="408" r="7" fill="var(--thoughts-a)"/>
    <circle cx="536" cy="493" r="7" fill="var(--node)"/>

    <path d="M886 408 Q886 441 856 441 H659 Q639 441 639 461 V493" fill="none" stroke="var(--hopes-b)" stroke-width="2.5"/>
    <circle cx="886" cy="408" r="7" fill="var(--hopes-b)"/>
    <circle cx="639" cy="493" r="7" fill="var(--node)"/>

    <path d="M572 716 V748 Q572 768 552 768 H350 Q326 768 326 792 V800" fill="none" stroke="var(--emotions-b)" stroke-width="2.5"/>
    <circle cx="326" cy="800" r="7" fill="var(--emotions-b)"/>
    <circle cx="572" cy="716" r="7" fill="var(--node)"/>

    <path d="M604 716 V748 Q604 768 624 768 H827 Q851 768 851 792 V800" fill="none" stroke="var(--concerns-b)" stroke-width="2.5"/>
    <circle cx="851" cy="800" r="7" fill="var(--concerns-b)"/>
    <circle cx="604" cy="716" r="7" fill="var(--node)"/>
  </svg>

  <section class="card card--thoughts">
    <h2 class="card__title">THOUGHTS</h2>
    <p class="card__row"><span class="prompt">It seems…</span><span class="prompt prompt--strong">I wonder…</span></p>
    <p class="card__row"><span class="prompt prompt--strong">It’s my opinion…</span><span class="prompt">I believe…</span></p>
    <p class="card__row"><span class="prompt">I assume…</span><span class="prompt prompt--strong">I think…</span></p>
  </section>

  <section class="card card--hopes">
    <h2 class="card__title">HOPES</h2>
    <p class="card__row"><span class="prompt prompt--strong">I hope…</span><span class="prompt">I wish…</span></p>
    <p class="card__row"><span class="prompt prompt--strong">It’s my desire…</span></p>
    <p class="card__row"><span class="prompt">I’d like to see…</span><span class="prompt prompt--strong">I want…</span></p>
    <p class="card__row"><span class="prompt">I need…</span></p>
  </section>

  <div class="hub"><h1 class="hub__title">NODE ASSIST</h1></div>

  <section class="card card--emotions">
    <h2 class="card__title">EMOTIONS</h2>
    <p class="card__row"><span class="prompt prompt--strong">I’m…</span><span class="prompt">hopeful…</span><span class="prompt prompt--strong">worried…</span></p>
    <p class="card__row"><span class="prompt">sad…</span><span class="prompt prompt--strong">afraid…</span><span class="prompt">mad…</span><span class="prompt prompt--strong">glad…</span></p>
    <p class="card__row"><span class="prompt">happy…</span><span class="prompt prompt--strong">confident…</span><span class="prompt">insecure…</span></p>
    <p class="card__row"><span class="prompt">lonely…</span><span class="prompt prompt--strong">bothered…</span></p>
    <p class="card__row"><span class="prompt">uncertain…</span></p>
  </section>

  <section class="card card--concerns">
    <h2 class="card__title">CONCERNS</h2>
    <p class="card__row"><span class="prompt prompt--strong">I worry about…</span></p>
    <p class="card__row"><span class="prompt">I’m afraid that…</span></p>
    <p class="card__row"><span class="prompt prompt--strong">I’m nervous because…</span></p>
    <p class="card__row"><span class="prompt">It bothers me that…</span></p>
  </section>
</main>
</body>
</html>
```